New web page design for our brand Casa Olmera

We have changed our logo and the image of our products, so we would like to redesign ,our web page as well according to the new design.
Our cosmetic products are based in nature and tradition, like they used to be prepared in the old pharmacies.
Our actual web is www.casaolmera.es, so we need similar estructure but completely different design.

Industry/Entity Type

Cosmetics

Number of Pages Required

5+ page

Requirements
Must have
• References to natural ingredients and also to old pharmacys or apothecaries.
Nice to have
• Nature images or old botanics drawings
• I would like to have a cover page with just an image saying welcome to Casa Olmera's world

```html
<!DOCTYPE html>
<html lang="en">
<head>
<meta charset="utf-8">
<title>About Us · Casa Olmera</title>
<link rel="stylesheet" href="https://fonts.googleapis.com/css2?family=Raleway:wght@300;400;600;700&family=Open+Sans:wght@400;600&display=swap">
<style>
  :root{
    --brown-dark:#3b2620;
    --brown:#4a3028;
    --brown-mid:#6b4a3c;
    --cream:#f4eee6;
    --paper:#faf7f2;
    --text:#5a4a42;
    --muted:#a8978c;
    --line:#d9cfc4;
    --white:#ffffff;
  }
  *{margin:0;padding:0;box-sizing:border-box}
  html,body{width:900px;height:1200px;overflow:hidden}
  body{background:var(--cream);font-family:"Open Sans",sans-serif;color:var(--text);position:relative}
  .site-header{height:60px;background:var(--paper);position:relative}
  .brand{position:absolute;left:72px;top:10px;display:flex;align-items:center;gap:8px;font-family:"Raleway",sans-serif;font-weight:700;font-size:19px;color:var(--brown-dark)}
  .brand-mark{width:14px;height:14px;border-radius:50%;background:var(--brown-dark)}
  .account-links{position:absolute;right:80px;top:8px;display:flex;gap:16px;font-size:8.5px;color:var(--muted)}
  .account-links span{display:flex;align-items:center;gap:4px}
  .account-links i{display:inline-block;width:7px;height:7px;border-radius:50%;background:var(--muted)}
  .search{position:absolute;right:80px;top:24px;width:180px;height:18px;border:1px solid var(--line);background:var(--white);font-size:8px;color:var(--muted);padding:3px 6px}
  .search svg{position:absolute;right:5px;top:4px}
  .main-nav{height:20px;background:var(--brown-dark);display:flex;justify-content:center;gap:62px;align-items:center;font-family:"Raleway",sans-serif;font-weight:600;font-size:8px;letter-spacing:.8px;color:var(--white)}
  .main-nav .active{background:var(--brown-mid);padding:6px 10px}
  .hero{height:262px;position:relative;background:linear-gradient(180deg,#b9ada2 0%,#8d7f74 55%,#6e625a 100%)}
  .hero-title{position:absolute;left:0;right:0;top:188px;text-align:center;font-family:"Raleway",sans-serif;font-weight:300;font-size:32px;letter-spacing:2px;color:var(--white)}
  .hero-arrow{position:absolute;top:118px}
  .hero-arrow.left{left:10px}.hero-arrow.right{right:10px}
  .about{padding:42px 72px 0 72px;background:var(--cream);height:678px}
  .about h2{font-family:"Raleway",sans-serif;font-weight:700;font-size:16px;color:var(--brown-dark);letter-spacing:.5px}
  .about-body{display:flex;gap:38px;margin-top:22px}
  .about-photo{width:214px;height:340px;flex:none;background:linear-gradient(160deg,#d8d2c8 0%,#9e8f80 50%,#4c3a30 100%);position:relative}
  .about-photo .caption{position:absolute;left:14px;bottom:14px;font-family:"Raleway",sans-serif;font-weight:600;font-size:13px;color:var(--white);line-height:1.3}
  .about-text p{font-size:9.4px;line-height:15px;margin-bottom:11px;text-align:justify}
  .site-footer{position:absolute;left:0;right:0;top:1020px;height:180px;background:var(--brown-dark);color:#cbbdb2}
  .footer-cols{display:flex;padding:20px 72px 0 72px;gap:30px}
  .footer-col h3{font-family:"Raleway",sans-serif;font-size:10px;font-weight:700;color:var(--white);margin-bottom:10px;letter-spacing:.4px}
  .footer-col p,.footer-col li{font-size:8px;line-height:13px}
  .footer-col ul{list-style:none}
  .col-about{width:160px}.col-links{width:110px}.col-news{width:220px}.col-contact{flex:1}
  .news-input{height:18px;background:var(--white);margin:8px 0 6px;width:200px}
  .news-btn{display:inline-block;background:var(--brown-mid);color:var(--white);font-size:8px;font-weight:600;padding:4px 12px}
  .contact-row{display:flex;gap:6px;align-items:center;margin-bottom:5px}
  .social{display:flex;gap:6px;margin:6px 0}
  .social span{width:12px;height:12px;background:var(--brown-mid)}
  .copyright{position:absolute;left:0;right:0;bottom:0;height:26px;border-top:1px solid #56392f;font-size:7.5px;padding:8px 72px;color:var(--muted)}
</style>
</head>
<body>
<header class="site-header">
  <div class="brand"><span class="brand-mark"></span>Casa Olmera</div>
  <div class="account-links"><span><i></i>My Account</span><span><i></i>Login</span><span><i></i>Checkout</span><span><i></i>Cart</span></div>
  <div class="search">SEARCH
    <svg width="9" height="9" viewBox="0 0 10 10"><circle cx="4" cy="4" r="3" fill="none" stroke="#a8978c" stroke-width="1.3"/><line x1="6.3" y1="6.3" x2="9" y2="9" stroke="#a8978c" stroke-width="1.3"/></svg>
  </div>
</header>
<nav class="main-nav"><span>HOME</span><span>CBD</span><span class="active">PRODUCT LINES</span><span>SERVICES</span><span>NEWS</span><span>CONTACT</span><span>SHOP</span></nav>
<section class="hero" role="img" aria-label="Hands preparing a cosmetic mixture in a laboratory flask">
  <svg class="hero-arrow left" width="14" height="24" viewBox="0 0 14 24"><polyline points="11,2 3,12 11,22" fill="none" stroke="#fff" stroke-width="2.5"/></svg>
  <svg class="hero-arrow right" width="14" height="24" viewBox="0 0 14 24"><polyline points="3,2 11,12 3,22" fill="none" stroke="#fff" stroke-width="2.5"/></svg>
  <h1 class="hero-title">ABOUT US</h1>
</section>
<main class="about">
  <h2>A FEW WORD ABOUT US</h2>
  <div class="about-body">
    <div class="about-photo" role="img" aria-label="Glass apothecary jar being filled with cream">
      <div class="caption">CASA OLMERA<br><span style="font-weight:400;font-size:10px">Apothecary Cosmetics</span></div>
    </div>
    <div class="about-text">
      <p>Casa Olmera was born in a small family pharmacy, where remedies were weighed by hand and every cream was mixed in the back room. We keep that patient way of working alive, combining old apothecary recipes with careful, modern quality controls for every single batch we prepare.</p>
      <p>Our formulas start with plants: olive, rosemary, calendula, lavender and almond, gathered from growers we know by name. We press, macerate and distil them slowly, as the old pharmacists did, so their natural properties reach your skin intact and gentle.</p>
      <p>Each product is made in short runs in our own workshop. Jars are filled, labelled and checked one by one, which lets us keep fresh ingredients, avoid needless additives and answer every question a customer may have about what goes inside.</p>
      <p>We believe that beauty care should be simple and honest. That is why our labels list every ingredient in plain words, why we never test on animals, and why our packaging is glass and paper that can be reused or recycled at home.</p>
      <p>Visiting our shop feels like stepping into a nineteenth century rebotica: wooden shelves, amber bottles and the scent of herbs drying on the counter. Our team will gladly guide you toward the cream, oil or soap that suits your skin and your daily routine.</p>
      <p>If you would like to learn more about our history, our growers or the way we work, write to us at any time. We answer every message personally and are always happy to share the small secrets of the old apothecary with you.</p>
    </div>
  </div>
</main>
<footer class="site-footer">
  <div class="footer-cols">
    <div class="footer-col col-about"><h3>ABOUT US</h3><p>We offer our customers natural cosmetics crafted in the tradition of the old apothecary, with care and honest ingredients.</p></div>
    <div class="footer-col col-links"><h3>QUICK LINKS</h3><ul><li>Link</li><li>Product lines</li><li>Services</li><li>News</li><li>Contact</li></ul></div>
    <div class="footer-col col-news"><h3>NEWSLETTER SIGN UP</h3><p>Register your email address to get news and special offers.</p><div class="news-input"></div><span class="news-btn">SIGN UP</span></div>
    <div class="footer-col col-contact"><h3>CONTACT US</h3>
      <div class="contact-row"><svg width="8" height="10" viewBox="0 0 8 10"><path d="M4 0a3.5 3.5 0 0 0-3.5 3.5C.5 6 4 10 4 10s3.5-4 3.5-6.5A3.5 3.5 0 0 0 4 0z" fill="#cbbdb2"/></svg><p>Calle de los Tilos 14, 46001 Valencia</p></div>
      <div class="social"><span></span><span></span><span></span><span></span><span></span></div>
      <div class="contact-row"><svg width="9" height="7" viewBox="0 0 9 7"><rect x=".5" y=".5" width="8" height="6" fill="none" stroke="#cbbdb2"/><polyline points=".5,.5 4.5,4 8.5,.5" fill="none" stroke="#cbbdb2"/></svg><p>hola@casaolmera.es</p></div>
    </div>
  </div>
  <div class="copyright">© Copyright 2017 Casa Olmera · www.casaolmera.es</div>
</footer>
</body>
</html>
```